Letterhead Design Project

I am the new owner of an existing Accouting and Financial Planning Firm (which I have been an employee at for 3 years)
We need to change the letterhead due to a change to the company's ABN etc., so thought we would like to modernise this at the same time.
We wish to keep the existing logo so there is familiarity to the clients. As per the notes on the attached document, we are happy to remove the wording from the logo, whichever will look better.
The letterhead needs to be professional, yet modern.
I will upload our logo and the required details for the letterhead.

Industry/Entity Type

Financial

Requirements
Must have
• Logo and provided business details.

```html
<!DOCTYPE html>
<html lang="en">
<head>
<meta charset="utf-8">
<title>Marlow Accountants &amp; Financial Services — Letterhead</title>
<link href="https://fonts.googleapis.com/css2?family=Open+Sans:wght@400;700&display=swap" rel="stylesheet">
<style>
  :root {
    --navy: #1f3f78;
    --brand-navy: #0c3a7d;
    --faint: #d9e1ea;
    --sheet-border: #333333;
    --paper: #ffffff;
  }
  * { margin: 0; padding: 0; box-sizing: border-box; }
  html, body { width: 1200px; height: 900px; overflow: hidden; background: var(--paper); }
  body { position: relative; font-family: "Open Sans", Arial, sans-serif; color: var(--navy); }

  .sheet {
    position: absolute; top: 62px; width: 528px; height: 747px;
    border: 1px solid var(--sheet-border); background: var(--paper);
  }
  .sheet--plain { left: 46px; }
  .sheet--branded { left: 619px; }

  .header-name {
    position: absolute; top: 34px; right: 415px;
    text-align: right; font-size: 12.5px; line-height: 16px; letter-spacing: 0.1px;
  }
  .header-rule {
    position: absolute; top: 38px; left: 118px; width: 1px; height: 66px; background: var(--navy);
  }

  .brand-mark {
    position: absolute; display: flex; align-items: center; gap: 6px;
  }
  .sheet--plain .brand-mark { top: 44px; left: 130px; }
  .sheet--branded .brand-mark { top: 44px; right: 28px; }
  .brand-mark__square { width: 22px; height: 22px; background: var(--brand-navy); }
  .brand-mark__name {
    font-weight: 700; font-size: 22px; letter-spacing: 1px; color: var(--brand-navy); line-height: 1;
  }

  .backdrop-name {
    position: absolute; top: 270px; left: 0; width: 100%; text-align: center;
    font-weight: 700; font-size: 104px; letter-spacing: 2px; color: var(--faint); line-height: 1;
  }

  .footer-address, .footer-contact {
    position: absolute; font-size: 9.4px; line-height: 12.2px; letter-spacing: 0.1px;
  }
  .footer-address { left: 33px; top: 679px; }
  .footer-contact { right: 30px; top: 655px; text-align: right; }
</style>
</head>
<body>

<section class="sheet sheet--plain" aria-label="Letterhead, plain version">
  <div class="header-name">MARLOW<br>ACCOUNTANTS<br>&amp; FINANCIAL<br>SERVICES</div>
  <div class="header-rule"></div>
  <div class="brand-mark">
    <span class="brand-mark__square"></span>
    <span class="brand-mark__name">MARLOW</span>
  </div>

  <address class="footer-address" style="font-style:normal">
    MARLOW ACCOUNTANTS &amp; FINANCIAL SERVICES<br>
    12 CARRINGTON STREET, BENDALE, VIC, 3699,<br>
    PO BOX 2210, RIVERTON, NSW, 2648
  </address>
  <address class="footer-contact" style="font-style:normal">
    ABN: 48 210 397 114<br>
    PH: 02 5550 1184<br>
    FAX: 02 5550 1185<br>
    EMAIL: ADMIN@MARLOWACCOUNTANTS.COM.AU<br>
    WWW.MARLOWACCOUNTANTS.COM.AU
  </address>
</section>

<section class="sheet sheet--branded" aria-label="Letterhead, version with background brand name">
  <div class="brand-mark">
    <span class="brand-mark__square"></span>
    <span class="brand-mark__name">MARLOW</span>
  </div>

  <div class="backdrop-name" aria-hidden="true">MARLOW</div>

  <address class="footer-address" style="font-style:normal">
    MARLOW ACCOUNTANTS &amp; FINANCIAL SERVICES<br>
    12 CARRINGTON STREET, BENDALE, VIC, 3699,<br>
    PO BOX 2210, RIVERTON, NSW, 2648
  </address>
  <address class="footer-contact" style="font-style:normal">
    ABN: 48 210 397 114<br>
    PH: 02 5550 1184<br>
    FAX: 02 5550 1185<br>
    EMAIL: ADMIN@MARLOWACCOUNTANTS.COM.AU<br>
    WWW.MARLOWACCOUNTANTS.COM.AU
  </address>
</section>

</body>
</html>
```